Ridgeway Teen Circle (Flyer)

I want a flyer to advertise my service.
Details below, and logo's to use are attached.

A girls only after school program, 11-14yrs, as OSHC is no longer avail, dedicated to coaching & mentoring our girls into strong, independent young women.

The Brainchild of Rebecca Tolland, Ridgeway Teen Circle was created to address the growing demand for after school/school holiday supervision for kids moving from primary into high school, when OSHC ceases to exist.
With over 12 years experience mentoring and coaching young women in the corporate world, Bec decided to leave her role as a Director with Corlana Bank, and follow her passion.
Bec, along with her sister Jocelyn, who has over 10 years experience in local communities as a Youth Worker, and is also a qualified Enrolled Nurse, embarked on building a program designed to keep parents happy (by knowing their girls are safe) and dedicated to coaching and mentoring our girls into strong, independent young women.
Open every afternoon and during school holidays, we look to offer;
- Daily meditation
- Healthy snacks
- Dedicated homework time
- Organised group activity, led by qualified instructors (yoga, fitness class, soccer etc)
- Regular guests speakers, addressing issues/concerns for young people today
- SOCIAL MEDIA FREE ZONE

Located 317 Pembury Rd, Baulkham Hills (across from Ardmore Private Hospital)
Open 3-6pm Monday to Friday

Facebook page: http://circle.example/ridgewayteencircle
Email: info@ridgewayteencircle.example.com.au
Mobile: 0400555183

Target Market(s)

Parents of teenage girls, teenage girls 11-14 years

Industry/Entity Type

School

Font styles to use
Sans Serif

Colors
b768aa
e667a6

Requirements
Must have
• What progam is - see brief
• Who runs it
Should not have
• Not be too busy, not overly mature images

```html
<!DOCTYPE html>
<html lang="en">
<head>
<meta charset="utf-8">
<title>Ridgeway Teen Circle – After School Program Flyer</title>
<link rel="stylesheet" href="https://fonts.googleapis.com/css2?family=Arimo:wght@400;700&display=swap">
<style>
  :root {
    --hot-pink: #ec1c8c;
    --rose: #e667a6;
    --orchid: #b768aa;
    --plum: #9a3d98;
    --violet-band: #a54fb4;
    --ink: #1f1d33;
    --white: #ffffff;
  }
  * { margin: 0; padding: 0; box-sizing: border-box; }
  html, body { width: 874px; height: 1200px; overflow: hidden; background: var(--white); }
  .flyer {
    position: relative;
    width: 874px;
    height: 1200px;
    overflow: hidden;
    font-family: "Arimo", Arial, sans-serif;
    font-weight: 400;
    background: linear-gradient(160deg, #f3e1f1 0%, #faf4fa 35%, #f1e6f4 65%, #f8eef6 100%);
  }
  .backdrop { position: absolute; inset: 0; }
  .headline {
    position: absolute; left: 0; width: 874px; text-align: center;
    font-weight: 400; color: var(--hot-pink);
    text-shadow: 3px 3px 0 rgba(154, 61, 152, 0.55);
    line-height: 1; white-space: nowrap;
  }
  .headline--main { top: 17px; font-size: 112px; letter-spacing: -3px; }
  .headline--sub { top: 101px; font-size: 60px; letter-spacing: -1.5px; }
  .rule { position: absolute; left: 28px; width: 818px; height: 3px; background: var(--violet-band); }
  .rule--top { top: 172px; }
  .rule--bottom { top: 252px; }
  .tagline {
    position: absolute; top: 180px; left: 0; width: 874px; text-align: center;
    font-size: 27.5px; line-height: 37px; color: var(--plum); letter-spacing: -0.6px;
  }
  .tagline .accent { color: var(--hot-pink); }
  .story-band { position: absolute; left: 0; top: 268px; width: 874px; height: 440px; }
  .story {
    position: absolute; top: 294px; left: 18px; width: 824px;
    text-align: justify; text-align-last: center; hyphens: auto;
    font-size: 22px; line-height: 27.7px; color: var(--hot-pink); letter-spacing: -0.7px;
  }
  .story span { display: block; }
  .offer-tab { position: absolute; left: 0; top: 645px; width: 326px; height: 36px; }
  .offer-tab__label {
    position: absolute; top: 647px; left: 54px; font-size: 27px; color: var(--white);
  }
  .offer-list {
    position: absolute; top: 683px; left: 22px; list-style: none;
    font-size: 28.5px; line-height: 37.2px; color: #c4409b; letter-spacing: -0.3px;
  }
  .offer-list li { position: relative; padding-left: 32px; }
  .offer-list li::before {
    content: ""; position: absolute; left: 2px; top: 12px; width: 13px; height: 13px;
    border-radius: 50%; background: var(--violet-band);
  }
  .offer-list .highlight { color: var(--hot-pink); }
  .location-band {
    position: absolute; left: 20px; top: 989px; width: 838px; height: 71px;
    background: var(--violet-band); color: var(--white); text-align: center;
    font-size: 23.3px; line-height: 31px; padding-top: 5px; letter-spacing: -0.4px;
    white-space: nowrap;
  }
  .contact {
    position: absolute; left: 40px; width: 660px; text-align: center; color: var(--rose);
    font-size: 29px; letter-spacing: -0.3px; line-height: 1; white-space: nowrap;
  }
  .contact--email { top: 1073px; font-size: 27px; }
  .contact--mobile { top: 1112px; }
  .contact--web {
    top: 1149px; left: 140px; width: auto; text-align: left;
    font-size: 31px; color: #d9349a;
  }
  .web-marker {
    position: absolute; left: 87px; top: 1147px; width: 36px; height: 36px; background: var(--orchid);
  }
  .brand-name {
    position: absolute; left: 706px; top: 1090px; width: 150px; text-align: center;
    font-size: 25px; line-height: 28px; font-weight: 700; color: var(--hot-pink);
  }
  .foot-strip { position: absolute; left: 0; top: 1192px; width: 874px; height: 8px; background: var(--rose); }
</style>
</head>
<body>
<main class="flyer">
  <div class="backdrop" role="img" aria-label="Soft pastel pink and lilac brushstroke background texture"></div>

  <h1 class="headline headline--main">A GIRLS ONLY</h1>
  <h2 class="headline headline--sub">AFTER SCHOOL PROGRAM</h2>

  <div class="rule rule--top"></div>
  <p class="tagline">11-14yrs, as OSHC is no longer avail, <span class="accent">dedicated to coaching &amp;<br>mentoring our girls into strong, independent young women.</span></p>
  <div class="rule rule--bottom"></div>

  <svg class="story-band" viewBox="0 0 874 440" aria-hidden="true">
    <path d="M0 30 L40 24 L120 30 L300 18 L520 26 L700 12 L874 20 L874 420 L820 426 L700 412 L640 422 L600 360 L520 368 L300 372 L40 380 L0 376 Z" fill="#1f1d33"/>
  </svg>
  <div class="story">
    <span>The Brainchild of Rebecca Tolland, Ridgeway Teen Circle was created to address the growing demand for after school/school holiday supervision for kids moving from primary into high school, when OSHC ceases to exist.</span>
    <span>With over 12 years experience mentoring and coaching young women in the corporate world, Bec decided to leave her role as a Director with Corlana Bank, and follow her passion.</span>
    <span>Bec, along with her sister Jocelyn, who has over 10 years experience in local communities as a Youth Worker, and is also a qualified Enrolled Nurse, embarked on building a program designed to keep parents happy (by knowing their girls are safe) and dedicated to coaching and mentoring our girls into strong, independent young women.</span>
    <span>Open every afternoon and during school holidays</span>
  </div>

  <svg class="offer-tab" viewBox="0 0 326 36" aria-hidden="true">
    <polygon points="0,0 310,0 326,36 0,36" fill="#b768aa"/>
  </svg>
  <span class="offer-tab__label">we look to offer :</span>

  <ul class="offer-list">
    <li>Daily meditation</li>
    <li>Healthy snacks</li>
    <li>Dedicated homework time</li>
    <li>Organised group activity, led by qualified instructors<br>(yoga, fitness class, soccer etc)</li>
    <li>Regular guests speakers, addressing issues/concerns for<br>young people today</li>
    <li class="highlight">SOCIAL MEDIA FREE ZONE</li>
  </ul>

  <div class="location-band">Located 317 Pembury Rd, Baulkham Hills (across from Ardmore Private Hospital)<br>Open 3-6pm Monday to Friday</div>

  <p class="contact contact--email">Email: info@ridgewayteencircle.example.com.au</p>
  <p class="contact contact--mobile">Mobile: 0400555183</p>
  <span class="web-marker" aria-hidden="true"></span>
  <p class="contact contact--web">http://circle.example/ridgewayteencircle</p>

  <p class="brand-name">Ridgeway Teen Circle</p>

  <div class="foot-strip"></div>
</main>
</body>
</html>
```